Harbor Crest Data Systems Needs a Website Desing

We need a website design for a new company based in Kuwait called Harbor Crest Data Systems (HCDS). We provide Software as a Service (SaaS) solutions for small and medium business companies. We will develop the required E-systems like HR,Payroll,Accounting Systems for those customers who wants to focus on their business instead of wasting time to automate it. HCDS need a web site that represent this activity and showing our cloud products and allow out customers to easily identify their needs. as a normal web site basic things need to be included like :
about HCDS
Solutions
PressRoom
Contact us
please i need something similar to trelvoxa.com or qup.com or www.dro7lak.com with blue and black theme .. please check the Company's logo
Updates
hi all ,,,
the project is only design without any codes
Reason: The project is focus on design only ,, i will be really appreciated to have more designs

```html
<!DOCTYPE html>
<html lang="en">
<head>
<meta charset="utf-8">
<title>Harbor Crest Data Systems</title>
<link rel="stylesheet" href="https://fonts.googleapis.com/css2?family=Noto+Sans:wght@400;700&display=swap">
<style>
:root{
  --blue:#2f7cc6;
  --blue-dark:#2a6bb5;
  --blue-band:#3e9ad6;
  --sky-top:#4a8fd6;
  --sky-light:#d6e7f5;
  --text:#555;
  --grey-text:#6a6a6a;
  --side-1:#e4e4e4;
  --side-2:#d2d2d2;
  --solutions:#a3c4e4;
  --solutions-text:#35628f;
  --white:#fff;
}
*{box-sizing:border-box;margin:0;padding:0}
html,body{width:1132px;height:1200px;overflow:hidden}
body{position:relative;background:var(--white);font-family:"Noto Sans",Tahoma,sans-serif;color:var(--text)}
.abs{position:absolute}

.site-header{left:0;top:0;width:1132px;height:142px;background:linear-gradient(180deg,#2c78c6 0%,#4a94da 70%,#3a83cc 100%)}
.logo-box{left:38px;top:17px;width:422px;height:104px;background:var(--white);display:flex;align-items:center;padding-left:24px;gap:18px}
.logo-dot{width:70px;height:70px;border-radius:50%;background:var(--blue)}
.logo-text{color:#1e1e1e;font-weight:700;line-height:1}
.logo-text .abbr{font-size:52px;letter-spacing:2px;display:block}
.logo-text .full{font-size:12.5px;display:block;margin-top:4px}
.top-links{left:520px;top:51px;display:flex;gap:16px;color:var(--white);font-size:12.5px}
.top-links span{display:flex;align-items:center;gap:6px}

.hero{left:0;top:142px;width:1132px;height:383px;background:linear-gradient(180deg,#a9c8ea 0%,#dbe9f6 55%,#e9f1f9 100%)}
.hero-photo{left:393px;top:0;width:739px;height:383px;background:linear-gradient(110deg,rgba(233,241,249,0) 0%,#c5d9ee 25%,#b8cfe6 60%,#e4edf6 100%)}
.hero-title{left:49px;top:60px;font-size:49px;color:var(--blue);font-weight:400}
.hero-copy{left:49px;top:144px;font-size:26px;line-height:31.5px;color:var(--grey-text)}
.btn-demo{left:49px;top:266px;width:131px;height:36px;border:1px solid #a8a8a8;border-radius:3px;background:linear-gradient(#fafafa,#cfcfcf);font-size:15px;color:#555;display:flex;align-items:center;justify-content:center;gap:6px}

.main-nav{left:0;top:525px;width:1132px;height:70px;background:linear-gradient(180deg,#47a8e0 0%,#3a97d6 50%,#2f7cc6 52%,#3485cc 100%);display:flex;padding-left:49px}
.main-nav a{color:var(--white);text-decoration:none;font-size:18.5px;display:flex;align-items:center;height:70px;border-left:1px dotted rgba(255,255,255,.35);padding:0 28px 0 28px;gap:16px}
.main-nav a:last-child{border-right:1px dotted rgba(255,255,255,.35)}
.main-nav a::before{content:"›";font-size:16px}

.welcome-title{left:49px;top:632px;font-size:49px;color:var(--blue);line-height:1}
.welcome-sub{left:49px;top:692px;font-size:29px;color:#777}
.rule{left:49px;top:740px;width:676px;height:1px;background:#aaa}
.article-icon{left:49px;top:764px;width:130px;height:123px;background:linear-gradient(135deg,#e6e6e6,#9a9a9a);border-radius:4px}
.article{left:201px;top:764px;width:520px}
.article h3,.news h3{font-size:16.5px;color:var(--blue);font-weight:700;margin-bottom:4px}
.article p{font-size:12px;line-height:22.4px;color:#444}
a.inline{color:var(--blue)}

.solutions{left:49px;top:920px;width:676px;height:193px;background:var(--solutions)}
.solutions h2{position:absolute;left:22px;top:22px;font-size:29px;font-weight:400;color:#555}
.solutions h3{position:absolute;left:22px;top:82px;font-size:16.5px;color:var(--solutions-text);font-weight:700}
.solutions p{position:absolute;left:22px;top:114px;font-size:12px;line-height:22.4px;color:var(--solutions-text);width:430px}
.solutions .doc-icon{position:absolute;left:527px;top:24px;width:126px;height:144px;background:linear-gradient(160deg,#f4f4f4 0%,#d9d9d9 60%,#2a5fb0 100%);border-radius:3px}

.side-news{left:781px;top:595px;width:351px;height:332px;background:var(--side-1)}
.side-profile{left:781px;top:927px;width:351px;height:225px;background:var(--side-2)}
.side-title{font-size:30px;font-weight:400;color:#555}
.news{position:absolute;left:35px;top:40px;width:280px}
.news .side-title{margin-bottom:22px}
.news h3{line-height:22px}
.news p{font-size:12px;line-height:22.4px;color:#444}
.btn-more{display:inline-flex;align-items:center;justify-content:center;width:76px;height:22px;background:linear-gradient(#fff,#e6e6e6);border:1px solid #c8c8c8;font-size:11.5px;color:#444}
.news .btn-more{margin-top:30px}
.profile{position:absolute;left:35px;top:36px;width:290px}
.profile p{font-size:16px;line-height:22.5px;color:#777;margin-top:24px}
.profile .btn-more{margin-top:30px}
.profile-icon{position:absolute;left:235px;top:96px}

.site-footer{left:0;top:1152px;width:1132px;height:48px;background:linear-gradient(180deg,#3a97d6,#2f7cc6);color:var(--white);font-size:12px}
.site-footer .copy{position:absolute;left:61px;top:16px}
.site-footer .legal{position:absolute;left:790px;top:16px}
.site-footer .legal a{color:var(--white)}
</style>
</head>
<body>
<header class="site-header abs">
  <div class="logo-box abs">
    <div class="logo-dot"></div>
    <div class="logo-text"><span class="abbr">HCDS</span><span class="full">Harbor Crest Data Systems</span></div>
  </div>
  <nav class="top-links abs">
    <span><svg width="12" height="12" viewBox="0 0 12 12" fill="none" stroke="#fff"><path d="M1 6 6 1l5 5M2.5 5v6h7V5"/></svg>to main page</span>
    <span><svg width="12" height="10" viewBox="0 0 12 10" fill="none" stroke="#fff"><rect x=".5" y=".5" width="11" height="9"/><path d="M.5 .5 6 5l5.5-4.5"/></svg>send e-mail</span>
  </nav>
</header>

<section class="hero abs">
  <div class="hero-photo abs" role="img" aria-label="Photo of two smiling business people working at a laptop against a sky background"></div>
  <h1 class="hero-title abs">Greetings</h1>
  <p class="hero-copy abs">A clean template to<br>showcase your product,<br>service or application.</p>
  <span class="btn-demo abs">VIEW DEMO <svg width="8" height="8" viewBox="0 0 8 8"><path d="M1 1l6 3-6 3z" fill="#777"/></svg></span>
</section>

<nav class="main-nav abs">
  <a href="#">HOME PAGE</a><a href="#">ABOUT US</a><a href="#">SERVICE</a><a href="#">PROJECTS</a><a href="#">SUPPORT</a><a href="#">CONTACTS</a>
</nav>

<h2 class="welcome-title abs">Welcome</h2>
<p class="welcome-sub abs">to our Business Company Site!</p>
<div class="rule abs"></div>
<div class="article-icon abs" role="img" aria-label="Illustration of a notebook with a curled page"></div>
<article class="article abs">
  <h3>Lorem ipsum dolor sit amet, contuer adipiscingelit</h3>
  <p>Sed diamaccusantium doloremque laudantium, totam rem aperiam eaquep. Store veritatis et quasi architecto <a class="inline" href="#">beatae vitae dicta sunt</a>, explicabo nemo enim ipsam voluptatem, quia voluptas sit, aspernatur aut odit aut fugitfeugiat nulla facilisis at vero eros et accumsan et iusto odio dignissim qui blandit. voluptas sit, aspernatur aut odit aut fugitfeugiat nulla facilisis at vero eros et accumsan et iusto odio dignissim qui blandit.</p>
</article>

<section class="solutions abs">
  <h2>Business Solutions</h2>
  <h3>Lorem ipsum dolor sit amet, contuer adipiscingelit</h3>
  <p>Sed diamaccusantium doloremque laudantium, totam rem aperiam eaquep. Store veritatis et quasi architecto beatae vitae dicta sunt, explicabo.</p>
  <div class="doc-icon" role="img" aria-label="Illustration of a handwritten letter with a blue info badge"></div>
</section>

<aside class="side-news abs">
  <div class="news">
    <h2 class="side-title">News &amp; Evenets</h2>
    <h3>Lorem ipsum dolor sit amet, contuer adipiscingelit</h3>
    <p>Sed diamaccusantium doloremque laudantium, totam rem aperiam eaquep. Store veritatis et quasi architecto beatae vitae dicta sunt, <a class="inline" href="#">explicabo nemo enim ipsam</a> voluptatem, quia voluptas sit, aspernatur</p>
    <span class="btn-more">read more</span>
  </div>
</aside>
<aside class="side-profile abs">
  <div class="profile">
    <h2 class="side-title">Company Profile</h2>
    <p>Lorem ipsum dolor sit<br>amet contuer</p>
    <span class="btn-more">read more</span>
  </div>
  <svg class="profile-icon" width="72" height="72" viewBox="0 0 72 72"><circle cx="36" cy="34" r="33" fill="#3cb4d4"/><circle cx="36" cy="20" r="5" fill="#fff"/><rect x="31" y="29" width="10" height="25" rx="2" fill="#fff"/></svg>
</aside>

<footer class="site-footer abs">
  <span class="copy">© 2013 Your Corporation. All rights reserved</span>
  <span class="legal"><a href="#">Terms of Use</a> | <a href="#">Privacy Statement</a></span>
</footer>
</body>
</html>
```